Broschüren-Design für Schuhmanufaktur
Zielgruppe
Schuhmanufaktur für Maßschuhe möchte sich modernisieren.
Aufgabenstellung
Maße und andere Daten entnehmen Sie sich den angefügten Daten und Bildern.
Es soll eine Broschüre (Maße etc in daten und skizze) und ein Plakat mit composing erstellt werden.
Offene Daten erwünscht (.ai)

```html
<!DOCTYPE html>
<html lang="de">
<head>
<meta charset="utf-8">
<title>Nahtwerk – Plakat 20 Jahre</title>
<link href="https://fonts.googleapis.com/css2?family=Quicksand:wght@300;400;600;700&display=swap" rel="stylesheet">
<style>
  :root {
    --page-bg: #f2f2f2;
    --white: #ffffff;
    --label-bg: rgba(92, 52, 34, 0.72);
    --panel-grey: #353535;
    --panel-brown: #2b1b16;
    --text-soft: #d9d9d9;
    --photo-dark: #2c1f1a;
    --photo-mid: #6e4631;
    --photo-warm: #a8694a;
    --photo-light: #c98a66;
  }
  * { box-sizing: border-box; margin: 0; padding: 0; }
  html, body { width: 1200px; height: 848px; overflow: hidden; }
  body {
    background: var(--page-bg);
    font-family: "Quicksand", sans-serif;
    position: relative;
  }
  .poster {
    position: absolute;
    left: 338px;
    top: 24px;
    width: 524px;
    height: 800px;
    background: var(--panel-grey);
    box-shadow: 0 6px 24px rgba(0,0,0,0.18);
    overflow: hidden;
  }
  .poster__photo {
    position: absolute;
    inset: 0 0 auto 0;
    height: 640px;
    background:
      radial-gradient(ellipse at 62% 28%, var(--photo-light) 0%, transparent 42%),
      radial-gradient(ellipse at 22% 88%, var(--photo-warm) 0%, transparent 38%),
      linear-gradient(160deg, var(--photo-dark) 0%, var(--photo-mid) 45%, var(--photo-dark) 100%);
  }
  .brand {
    position: absolute;
    left: 32px;
    top: 44px;
    display: flex;
    align-items: center;
    gap: 10px;
    color: var(--white);
    font-weight: 600;
    font-size: 26px;
  }
  .brand__dot {
    width: 34px; height: 34px;
    border-radius: 50%;
    background: var(--white);
  }
  .headline {
    position: absolute;
    left: 14px;
    top: 254px;
    display: flex;
    flex-direction: column;
    align-items: flex-start;
  }
  .headline__line {
    background: var(--label-bg);
    color: var(--white);
    padding: 0 6px;
    line-height: 1.1;
  }
  .headline__line--big { font-size: 56px; font-weight: 700; }
  .headline__line--name { font-size: 33px; font-weight: 700; margin-top: 8px; }
  .headline__line--claim { font-size: 34px; font-weight: 300; margin-top: 4px; }
  .headline__gap { height: 34px; }
  .services {
    position: absolute;
    left: 0; right: 0; bottom: 0;
    height: 160px;
    display: grid;
    grid-template-columns: repeat(3, 1fr);
  }
  .service {
    background: var(--panel-grey);
    text-align: center;
    padding: 24px 8px 0;
    color: var(--text-soft);
  }
  .service--accent { background: var(--panel-brown); }
  .service__title {
    color: var(--white);
    font-weight: 600;
    font-size: 19px;
    letter-spacing: 0.3px;
    margin-bottom: 6px;
  }
  .service__text {
    font-weight: 400;
    font-size: 15.5px;
    line-height: 1.35;
  }
</style>
</head>
<body>
  <main class="poster">
    <div class="poster__photo" role="img" aria-label="Composing aus Schuhleisten aus Holz, einem schwarzen Lederschuh, Lederzuschnitten und Werkzeug auf einer Werkbank"></div>

    <div class="brand">
      <span class="brand__dot"></span>
      <span class="brand__name">Nahtwerk</span>
    </div>

    <div class="headline">
      <span class="headline__line headline__line--big">20 JAHRE</span>
      <span class="headline__line headline__line--name">SCHUHMANUFAKTUR</span>
      <span class="headline__line headline__line--name">NAHTWERK</span>
      <span class="headline__gap"></span>
      <span class="headline__line headline__line--claim">Leder ist unsere</span>
      <span class="headline__line headline__line--claim">Leidenschaft</span>
    </div>

    <section class="services">
      <div class="service">
        <h2 class="service__title">REPARATUR</h2>
        <p class="service__text">Wir ermöglichen<br>hochwertigen<br>Lederwaren lange<br>Nutzbarkeit</p>
      </div>
      <div class="service service--accent">
        <h2 class="service__title">OPTIMIERUNG</h2>
        <p class="service__text">Wir übernehmen<br>spezielle<br>Anpassungswünsche</p>
      </div>
      <div class="service">
        <h2 class="service__title">KREATION</h2>
        <p class="service__text">Wir fertigen<br>individuelle<br>Maßschuhe</p>
      </div>
    </section>
  </main>
</body>
</html>
```